Sales Flyer or Trifold for selling our Monthly Computer Service

I need a flyer designed for our new monthly computer maintenance service. We have been using this software package for 3 years for business customers with much success, but now we want to sell this to individual residential clients with the idea that we can keep their computer safe, running well, and less of a hassle for them. It also will create a steady work load for my technicians, and stable recurring income.

I tried making something, but it is too amateur looking. The final design should look professional, be engaging, and draw from our existing web design, logos, business cards and such. Most importantly, it should make them see value in spending $29 per month to be part of the program. I will upload as much examples of other branding as I can to give you something to go off of. We try to use open sans for text. You should also visit quillfernpc.com for our current design scheme. I anticipate that we may go through a few revisions on this, and that I will probably have other similar signage created with complimentary designs later.

Reason: I am still needing some revisions from designers.

Target Market(s)

My target market is local affluent residential customers in the middle aged and up age range. People who may be or have been used to having tech support at their office.

Industry/Entity Type

Computer Repair

Font styles to use
Sans Serif

Requirements
Must have
• mention the components of the service that we offer. my existing flyer shows all of those. we also must use the logo in some way. It should have our contact information on the flyer too.
Nice to have
• I'm not sure yet, I really can't picture what I want. I am thinking a trifold. Maybe a single pager...
Should not have
• Please, please, no people with headsets on in a call center, no horrible stock imagery. We are trying to show that we are NOT a faceless call center, but instead give off a feeling of personalized support. We want to be their tech guy. Also, please do not use words with negative connotations like 'service plan' or similar. There are a lot of scammers out there claiming to do something similar and we need to disassociate ourselves as much as we can from them.

```html
<!DOCTYPE html>
<html lang="en">
<head>
<meta charset="utf-8">
<title>Quillfern PC – Steady Guard Trifold</title>
<link rel="stylesheet" href="https://fonts.googleapis.com/css2?family=Open+Sans:ital,wght@0,400;0,600;0,700;1,400&family=Raleway:wght@400;500;600&display=swap">
<style>
  :root{
    --red:#d8232a;
    --dark:#3a3a3c;
    --blue:#1b9ad6;
    --ink:#2e2e30;
    --paper:#ffffff;
    --stage:#e4e4e4;
  }
  *{box-sizing:border-box;margin:0;padding:0}
  html,body{width:1001px;height:1200px;overflow:hidden;background:var(--stage)}
  body{position:relative;font-family:"Open Sans",Arial,sans-serif;color:var(--ink)}
  .spread{position:absolute;left:20px;width:960px;height:560px;background:var(--paper);box-shadow:0 6px 18px rgba(0,0,0,.18)}
  .spread--outside{top:25px}
  .spread--inside{top:615px}
  .panel{position:absolute;top:0;width:320px;height:560px;overflow:hidden}
  .panel + .panel{border-left:1px solid #e2e2e2}
  .panel--a{left:0}.panel--b{left:320px}.panel--c{left:640px}
  .shapes{position:absolute;inset:0;width:320px;height:560px}
  .abs{position:absolute}
  .heading{font-family:"Raleway",sans-serif;font-weight:500;text-transform:uppercase;line-height:1.1}

  /* outside – flap */
  .screen-shot{position:absolute;left:38px;top:20px;width:250px;height:108px;background:linear-gradient(#f4f6f8,#dfe4ea);border:1px solid #bcc3cc}
  .flap-copy{left:30px;top:140px;width:225px;color:#fff;font-size:11px;line-height:1.2}
  .flap-copy p + p{margin-top:8px}
  .mission-text{left:105px;top:331px;width:130px;text-align:center;color:#fff;font-size:13px}
  .flap-close{right:18px;top:468px;width:285px;text-align:right;font-weight:700;font-size:12px;line-height:1.2;color:var(--dark)}

  /* outside – mailing */
  .vert{position:absolute;transform:rotate(-90deg);transform-origin:left top;white-space:nowrap}
  .sender{left:20px;top:530px;font-size:11px;line-height:1.35}
  .sender .name{display:flex;align-items:center;gap:6px;color:var(--red);font-family:"Raleway",sans-serif;font-size:14px;text-transform:uppercase}
  .dot{width:14px;height:14px;border:2px solid var(--red);border-radius:50%;display:inline-block}
  .recipient{left:120px;top:300px;font-size:11px;line-height:1.3}
  .recipient b{font-weight:700}
  .contact{font-size:11px;line-height:1.35}
  .contact--phone{left:268px;top:540px}
  .contact--web{left:238px;top:280px}
  .contact--mail{left:290px;top:120px}

  /* outside – cover */
  .brand{left:45px;top:40px;width:110px;height:110px;display:flex;flex-direction:column;align-items:center;justify-content:center;gap:6px;color:#fff;font-family:"Raleway",sans-serif;font-size:11px;text-transform:uppercase;letter-spacing:1px;transform:rotate(28deg)}
  .brand .ring{width:36px;height:36px;border:3px solid var(--red);border-radius:50%}
  .cover-title{left:75px;top:192px;width:200px;color:#fff;font-size:20px;text-align:right;transform:rotate(28deg)}
  .cover-title .rule{display:block;height:2px;background:#fff;margin:6px 0 4px 30px}
  .cover-title small{display:block;font-size:12px;text-transform:none;line-height:1.2}
  .photo{position:absolute}
  .photo--cover{left:25px;top:385px;width:290px;height:175px;background:linear-gradient(135deg,#9b78c9 0%,#c8b6dd 55%,#b9bcc1 100%);clip-path:polygon(12% 0,60% 0,100% 55%,100% 100%,0 100%,0 20%)}

  /* inside – left */
  .expertise{left:40px;top:82px;width:240px;color:#fff;font-size:10px;font-weight:600;line-height:1.25;text-transform:uppercase;text-align:center;transform:rotate(-29deg)}
  .personal-it{left:120px;top:192px;width:130px;color:#fff;font-size:12px;text-align:center;transform:rotate(-30deg)}
  .features-side{left:25px;top:302px;width:270px;font-size:10px;line-height:1.25;transform:rotate(-20deg)}
  .photo--team{left:0;top:430px;width:320px;height:130px;background:linear-gradient(#3c3c3e,#161617);clip-path:polygon(0 32%,100% 0,100% 100%,0 100%)}

  /* inside – middle */
  .filter-text{left:55px;top:83px;width:180px;color:#fff;font-size:13px;transform:rotate(28deg)}
  .solution{left:30px;top:262px;width:270px;color:var(--red);font-weight:700;font-size:11px;line-height:1.15;transform:rotate(12deg);transform-origin:left top}
  .checklist{left:45px;top:303px;width:230px;list-style:none;transform:rotate(12deg);transform-origin:left top;font-size:11.5px;line-height:1.15}
  .checklist li{display:flex;gap:12px;align-items:flex-start;margin-bottom:9px}
  .num{flex:none;width:17px;height:17px;background:var(--blue);color:#fff;font-size:9px;font-weight:700;display:flex;align-items:center;justify-content:center;transform:rotate(-12deg)}

  /* inside – right */
  .thanks{left:28px;top:30px;color:var(--red);font-size:21px}
  .quotes{left:28px;top:86px;width:270px;font-size:11px;line-height:1.3}
  .quotes blockquote{font-style:italic}
  .quotes blockquote::before{content:"\201C";color:#aaa;font-size:14px;line-height:0;font-weight:700;margin-right:3px}
  .quotes blockquote::after{content:"\201D";color:#aaa;font-size:14px;line-height:0;font-weight:700;margin-left:3px}
  .quotes cite{display:block;font-style:normal;font-size:10.5px;margin:2px 0 9px 10px}
  .photo--customer{left:25px;top:222px;width:280px;height:180px;background:linear-gradient(180deg,#f3f3f3 0%,#e4e4e4 30%,#d82a2a 31%,#b81f24 100%);clip-path:polygon(20% 0,80% 0,100% 100%,0 100%)}
  .care-list{left:28px;top:420px;width:280px;font-size:11px;line-height:1.2}
</style>
</head>
<body>

<section class="spread spread--outside" aria-label="Trifold outside">
  <div class="panel panel--a">
    <svg class="shapes" viewBox="0 0 320 560" aria-hidden="true">
      <polygon points="0,0 180,0 320,220 320,250 160,445 0,445" fill="var(--dark)"/>
      <rect x="280" y="223" width="24" height="24" fill="var(--blue)" transform="rotate(40 292 235)"/>
      <rect x="102" y="292" width="136" height="136" fill="var(--red)" transform="rotate(45 170 360)"/>
    </svg>
    <div class="screen-shot" role="img" aria-label="System information window screenshot"></div>
    <div class="abs flap-copy">
      <p>We take care of Automatic Updates and Patch installation for Northwind OS. So you don't have to.</p>
      <p>We also manage many 3rd party software and plugins such as Brewscript, Sparkplay and many other to close security holes and eliminate the guesswork of which updates to install.</p>
    </div>
    <p class="abs heading mission-text">This would be a great place for a mission statement</p>
    <p class="abs flap-close">....and Steady Guard is more than just a collection of software. We also include a personalized one on one tutoring session to teach you how to safely navigate the internet and use your computer</p>
  </div>

  <div class="panel panel--b">
    <div class="vert sender">
      <span class="name"><span class="dot"></span>Quillfern PC</span>
      <span>1820 Alder Ridge Rd</span><br>
      <span>Fernvale, IA 50999</span>
    </div>
    <div class="vert recipient"><b>Recipient</b><br>Street Address<br>City, ST ZIP Code</div>
    <div class="vert contact contact--phone">555-010-4477<br>Fax Fax</div>
    <div class="vert contact contact--web">www.quillfernpc.com</div>
    <div class="vert contact contact--mail">info@quillfernpc.com</div>
  </div>

  <div class="panel panel--c">
    <svg class="shapes" viewBox="0 0 320 560" aria-hidden="true">
      <rect x="30" y="25" width="140" height="140" fill="var(--dark)" transform="rotate(28 100 95)"/>
      <rect x="210" y="80" width="130" height="130" fill="var(--blue)" transform="rotate(28 275 145)"/>
      <rect x="60" y="140" width="230" height="230" fill="var(--red)" transform="rotate(28 175 255)"/>
      <rect x="275" y="390" width="40" height="40" fill="var(--dark)" transform="rotate(28 295 410)"/>
    </svg>
    <div class="abs brand"><span class="ring"></span>Quillfern PC</div>
    <div class="abs heading cover-title">Computer<br>Protection &amp;<br>Security for<br>your home<span class="rule"></span><small>Protect what matters<br>most to your family</small></div>
    <div class="photo photo--cover" role="img" aria-label="Frustrated woman resting her head on her hand in front of a laptop"></div>
  </div>
</section>

<section class="spread spread--inside" aria-label="Trifold inside">
  <div class="panel panel--a">
    <svg class="shapes" viewBox="0 0 320 560" aria-hidden="true">
      <polygon points="0,150 270,0 320,60 320,110 60,250 0,250" fill="var(--dark)"/>
      <rect x="25" y="230" width="90" height="70" fill="var(--red)" transform="rotate(-30 70 265)"/>
      <rect x="110" y="180" width="150" height="80" fill="var(--blue)" transform="rotate(-30 185 220)"/>
    </svg>
    <p class="abs expertise">At Quillfern PC, we have years of experience protecting the computers &amp; networks of our commercial business clients. Now, we are making the same enterprise grade security and protection available to our home users for a flat monthly rate.</p>
    <p class="abs heading personal-it">It's like having your own personal IT department</p>
    <p class="abs features-side">- Centrally managed &amp; monitored antivirus &amp; antimalware to stop malicious zero-day threats before they have a chance to infect your computer.<br>- Centrally monitored online backups of your files, folders, or even the whole operating system to protect precious data that could be damaged by viruses, fire, theft, or other disasters.</p>
    <div class="photo photo--team" role="img" aria-label="Team of technicians in black company shirts"></div>
  </div>

  <div class="panel panel--b">
    <svg class="shapes" viewBox="0 0 320 560" aria-hidden="true">
      <rect x="40" y="40" width="210" height="170" fill="var(--red)" transform="rotate(28 145 125)"/>
      <polygon points="0,540 40,495 100,560 0,560" fill="var(--blue)"/>
      <rect x="155" y="520" width="30" height="30" fill="var(--red)" transform="rotate(28 170 535)"/>
    </svg>
    <p class="abs heading filter-text">Web filtering customizable to 4 different levels of protection to keep your family safe -- centrally managed</p>
    <p class="abs solution">A Complete Solution to keep your Computer and Precious Files Safe and Protected</p>
    <ol class="abs checklist">
      <li><span class="num">1</span>Commercial Grade Antivirus &amp; Antispyware</li>
      <li><span class="num">2</span>Online and Local File Backup</li>
      <li><span class="num">3</span>Malicious Website Filtering</li>
      <li><span class="num">4</span>Automatic Update Installation</li>
      <li><span class="num">5</span>Hardware and Software Trouble Monitoring</li>
      <li><span class="num">6</span>Priority Service with 20% off Labor Rates</li>
    </ol>
  </div>

  <div class="panel panel--c">
    <h2 class="abs heading thanks">A big thanks from<br>our customers</h2>
    <div class="abs quotes">
      <blockquote>Your company is the greatest. I can't imagine anyone living without you.</blockquote>
      <cite>- Very smart customer</cite>
      <blockquote>This style is named quote but you can also use it to call attention to an important piece of info.</blockquote>
      <cite>- Very smart customer #2</cite>
    </div>
    <div class="photo photo--customer" role="img" aria-label="Smiling girl in a red top holding an open laptop"></div>
    <p class="abs care-list">- 24x7x365 monitoring of critical Northwind OS services and hardware health, designed to alert you to problems BEFORE they happen.<br>- Automated maintenance cleaning of your computer to keep it running smooth.<br>- Discounted rates for on site or remote service calls for Steady Guard clients.</p>
  </div>
</section>

</body>
</html>
```